Established Mortgage Brokerage Needs Wordpress Site for Corporate website

We need a wordpress website designed for a well-established Mortgage Brokerage in Oakville, Ontario. Our firm provides residential and commercial mortgage solutions for clients in Ontario, Canada. The final design should communicate professionalism, reliability, trustworthiness, financial stability. Colour scheme should be in line with our logo per attached files.

Target Market(s)

End consumer is knowledgable. Will vary from working families to business professionals, looking for financing alternatives for various types of real estate.

Other font styles liked:
• Please keep in line with Logo

Colors
3277b5

Requirements
Must have
• Site will have 10 pages. Logo must be included.
• Navigation menue will consist of Home, About, Services (with 3 pages in drop down Services offered, Mortgage FAQ and Realotrs), Calculators, Apply Now , Blog and Contact.
• Font should be in line with logo.
Nice to have
• Bright pictures, simplicity, and overall feeling of professionalism/knowledge.

```html
<!DOCTYPE html>
<html lang="en">
<head>
<meta charset="utf-8">
<title>Maplecrest Mortgage Group</title>
<link href="https://fonts.googleapis.com/css2?family=Open+Sans:wght@400;600;700&display=swap" rel="stylesheet">
<style>
:root{
  --blue:#2a8cd8;
  --blue-dark:#1f74b8;
  --red:#dc4640;
  --ink:#2b2b2b;
  --text:#555;
  --muted:#888;
  --grey-bg:#ececec;
  --card:#e4e4e4;
  --line:#d8d8d8;
  --footer:#3a3c40;
  --footer-deep:#333539;
  --white:#fff;
}
*{box-sizing:border-box;margin:0;padding:0}
html,body{width:1200px;height:3564px;overflow:hidden}
body{font-family:"Open Sans",Arial,sans-serif;color:var(--text);background:var(--white);font-size:14px;line-height:1.5}
.wrap{width:1072px;margin:0 auto;position:relative}
svg{display:block}

/* top bar */
.topbar{height:33px;background:var(--blue);color:var(--white);font-size:12px}
.topbar .wrap{display:flex;align-items:center;height:33px}
.topbar .contact-item{display:flex;align-items:center;gap:7px;margin-right:28px}
.topbar .social{margin-left:auto;display:flex;gap:16px}
.topbar .social span{width:9px;height:9px;border-radius:50%;background:rgba(255,255,255,.85)}

/* header */
.site-header{height:114px}
.site-header .wrap{display:flex;align-items:center;height:114px}
.brand{display:flex;align-items:center;gap:8px;font-weight:700;color:var(--blue);font-size:17px;letter-spacing:.5px}
.brand-square{width:26px;height:26px;background:var(--blue)}
.main-nav{margin-left:auto;display:flex;gap:38px;align-items:center;font-size:14px;font-weight:600;color:#333;margin-right:60px}

/* hero */
.hero{height:461px;position:relative;background:linear-gradient(100deg,#b9c4c9 0%,#d7cfc2 35%,#a9b7b0 62%,#6f9660 85%,#c98ab1 100%)}
.hero-caption{position:absolute;left:637px;top:138px}
.hero-caption p{display:inline-block;background:rgba(40,40,40,.72);color:var(--white);font-size:28px;font-weight:400;padding:2px 12px;margin-bottom:6px;line-height:1.3}
.btn-apply{display:inline-flex;align-items:center;gap:8px;background:var(--blue);color:var(--white);font-weight:700;font-size:15px;padding:7px 18px;margin-top:12px}

/* ask */
.ask{height:188px}
.ask .wrap{display:flex;padding-top:48px}
.ask h2{color:var(--blue);font-size:28px;font-weight:700;line-height:1.2;width:270px;padding-left:44px}
.ask h2 span{display:block;font-weight:400}
.ask-form{display:grid;grid-template-columns:repeat(3,232px);gap:14px 22px}
.field{height:33px;border:1px solid var(--line);font-size:12px;color:#aaa;padding:7px 10px;position:relative}
.field.select::after{content:"";position:absolute;right:10px;top:14px;border:4px solid transparent;border-top-color:#999}
.btn-submit{height:33px;background:var(--red);color:var(--white);font-weight:700;font-size:15px;text-align:center;line-height:33px}

/* features */
.features{height:375px;background:var(--grey-bg)}
.features .wrap{display:grid;grid-template-columns:repeat(4,1fr);padding-top:38px;text-align:center}
.feature{display:flex;flex-direction:column;align-items:center}
.feature-icon{width:86px;height:86px;border-radius:50%;background:var(--white);border:1px solid #ddd;display:flex;align-items:center;justify-content:center}
.feature h3{font-size:14px;font-weight:700;color:var(--ink);margin-top:22px;line-height:1.35;width:150px}
.feature p{font-size:12.5px;width:190px;margin-top:8px;line-height:1.5}
.feature .more{font-size:10px;color:var(--ink);margin-top:6px}
.btn-pill{background:var(--blue);color:var(--white);font-size:12.5px;border-radius:16px;padding:5px 16px;margin-top:10px}

/* commercial */
.commercial{height:737px;text-align:center}
.section-title{font-size:22px;font-weight:700;color:var(--ink);padding-top:62px;letter-spacing:.3px}
.section-lead{font-size:13px;width:860px;margin:14px auto 0;line-height:1.6}
.property-grid{display:grid;grid-template-columns:repeat(4,251px);gap:30px 22px;margin-top:72px;text-align:left}
.property-card{background:var(--card)}
.property-card .photo{height:150px}
.property-card .label{height:74px;display:flex;align-items:center;justify-content:space-between;padding:0 12px;font-size:14px;font-weight:600;color:var(--ink)}
.property-card .label b{font-size:18px}

/* welcome */
.welcome{height:485px;background:var(--grey-bg)}
.welcome .wrap{display:flex;padding-top:45px}
.welcome-text{width:490px}
.welcome-text h2{font-size:22px;font-weight:700;color:var(--ink)}
.welcome-text h3{font-size:16px;font-weight:700;color:var(--ink);margin-top:14px}
.welcome-text p{font-size:12.5px;margin-top:10px;line-height:1.6;text-align:justify}
.btn-square{display:inline-block;background:var(--blue);color:var(--white);font-size:12.5px;padding:8px 26px;margin-top:20px}
.link-grid{margin-left:68px;display:grid;grid-template-columns:245px 245px;gap:10px 10px}
.link-tile .photo{height:145px}
.link-tile span{display:block;font-size:13px;color:var(--ink);margin-top:10px;margin-bottom:8px}

/* news */
.news{height:506px;text-align:center}
.news .section-title{padding-top:50px}
.news .section-lead{margin-top:4px}
.news-grid{display:grid;grid-template-columns:repeat(3,336px);gap:32px;margin-top:46px;text-align:left}
.news-card .photo{height:178px}
.news-card h3{font-size:14px;font-weight:600;color:var(--ink);margin-top:18px}
.news-card p{font-size:12.5px;margin-top:10px;line-height:1.55}
.news-card .more{display:block;text-align:right;color:var(--blue);font-size:12.5px;margin-top:10px}

/* testimonials */
.testimonials{height:285px;background:linear-gradient(180deg,#3d98dd,#2a8ad6);color:var(--white);text-align:center;position:relative}
.testimonials h2{font-size:22px;font-weight:700;padding-top:26px}
.testimonials blockquote{width:910px;margin:12px auto 0;font-size:13px;line-height:1.8}
.avatar{width:52px;height:52px;border-radius:50%;background:#dfe8ef;border:2px solid var(--white);margin:8px auto 0}
.testimonials .name{font-size:13px;font-weight:600;margin-top:6px}
.testimonials .role{font-size:11px}
.dots{display:flex;justify-content:center;gap:6px;margin-top:10px}
.dots span{width:11px;height:11px;border-radius:50%;background:var(--white)}
.dots span.off{background:transparent;border:2px solid var(--white)}

/* footer */
.site-footer{height:380px;background:var(--footer);color:#aaa;font-size:11.5px}
.site-footer .wrap{display:flex;padding-top:25px;height:318px}
.footer-about{width:315px}
.footer-about .brand{font-size:14px}
.footer-about .brand-square{width:20px;height:20px}
.footer-about p{margin-top:30px;line-height:1.6;color:#6f7278}
.footer-about .more{color:var(--blue);margin-top:14px;display:block}
.footer-col{margin-left:60px}
.footer-col h4{color:var(--white);font-size:14px;font-weight:700;margin-top:26px;margin-bottom:14px}
.footer-links{list-style:none;width:130px}
.footer-links li{line-height:1.95}
.footer-links li::before{content:"›";color:var(--blue);margin-right:8px}
.tweet{display:flex;gap:8px;width:200px;margin-bottom:16px}
.tweet-thumb{width:34px;height:34px;background:#5a5d63;flex:none}
.tweet p{line-height:1.45}
.tweet a{color:var(--blue)}
.contact-list{width:200px;list-style:none}
.contact-list li{display:flex;gap:12px;margin-bottom:14px;line-height:1.5}
.contact-list svg{flex:none;margin-top:3px}
.footer-social{display:flex;gap:26px;margin-top:6px}
.footer-social span{width:8px;height:8px;border-radius:50%;background:#ccc}
.copyright{height:62px;background:var(--footer-deep);text-align:center;line-height:62px;font-size:11.5px;color:#aaa;border-top:1px solid #4a4d52}
</style>
</head>
<body>

<div class="topbar">
  <div class="wrap">
    <div class="contact-item">
      <svg width="12" height="12" viewBox="0 0 24 24"><path fill="#fff" d="M6.6 10.8a15 15 0 0 0 6.6 6.6l2.2-2.2c.3-.3.7-.4 1-.2 1.1.4 2.3.6 3.6.6.6 0 1 .4 1 1V20c0 .6-.4 1-1 1C10.6 21 3 13.4 3 4c0-.6.4-1 1-1h3.5c.6 0 1 .4 1 1 0 1.3.2 2.5.6 3.6.1.3 0 .7-.2 1z"/></svg>
      Need Support? 1-800-555-0142
    </div>
    <div class="contact-item">
      <svg width="13" height="10" viewBox="0 0 26 20"><rect x="1" y="1" width="24" height="18" fill="none" stroke="#fff" stroke-width="2"/><path d="M1 1l12 10 12-10" fill="none" stroke="#fff" stroke-width="2"/></svg>
      Email: info@maplecrest.example
    </div>
    <div class="social"><span></span><span></span><span></span><span></span></div>
  </div>
</div>

<header class="site-header">
  <div class="wrap">
    <div class="brand"><div class="brand-square"></div>MAPLECREST</div>
    <nav class="main-nav">
      <span>Home</span><span>AboutvServices</span><span>Calculater</span><span>Apply Now</span><span>Blog</span><span>Contact</span>
      <svg width="13" height="13" viewBox="0 0 20 20"><circle cx="8" cy="8" r="6" fill="none" stroke="#2a8cd8" stroke-width="2.5"/><path d="M12.5 12.5L18 18" stroke="#2a8cd8" stroke-width="2.5"/></svg>
    </nav>
  </div>
</header>

<section class="hero" role="img" aria-label="Smiling family of four sitting outside a house with a garden">
  <div class="hero-caption">
    <p>Whatever your Mortage Needs</p><br>
    <p>We Can Help</p><br>
    <span class="btn-apply">
      <svg width="8" height="10" viewBox="0 0 8 10"><path d="M0 0l8 5-8 5z" fill="#fff"/></svg>APPLY NOW
    </span>
  </div>
</section>

<section class="ask">
  <div class="wrap">
    <h2>ASK A<span>QUESTION</span></h2>
    <div class="ask-form">
      <div class="field">First Name</div>
      <div class="field">Last Name</div>
      <div class="field">E-mail</div>
      <div class="field">Phone</div>
      <div class="field select">How did you hear about us</div>
      <div class="btn-submit">SUBMIT</div>
    </div>
  </div>
</section>

<section class="features">
  <div class="wrap">
    <div class="feature">
      <div class="feature-icon"><svg width="30" height="26" viewBox="0 0 30 26"><path d="M15 2L2 13h4v11h7v-7h4v7h7V13h4z" fill="#2a8cd8"/></svg></div>
      <h3>Looking for a better mortgage?</h3>
      <p>Lorem ipsum dolor sit amet, consectetur adipiscing elit. Vestibulum et dignissim turpis. Maecenas</p>
      <span class="more">Read more</span><span class="btn-pill">REQUEST INFO</span>
    </div>
    <div class="feature">
      <div class="feature-icon"><svg width="24" height="30" viewBox="0 0 24 30"><rect x="1" y="1" width="22" height="28" rx="2" fill="#2a8cd8"/><rect x="4" y="4" width="16" height="6" fill="#fff"/><g fill="#fff"><rect x="4" y="13" width="4" height="3"/><rect x="10" y="13" width="4" height="3"/><rect x="16" y="13" width="4" height="3"/><rect x="4" y="18" width="4" height="3"/><rect x="10" y="18" width="4" height="3"/><rect x="16" y="18" width="4" height="3"/><rect x="4" y="23" width="4" height="3"/><rect x="10" y="23" width="4" height="3"/><rect x="16" y="23" width="4" height="3"/></g></svg></div>
      <h3>Looking for a better mortgage?</h3>
      <p>Lorem ipsum dolor sit amet, consectetur adipiscing elit. Vestibulum et dignissim turpis. Maecenas</p>
      <span class="more">Read more</span><span class="btn-pill">REQUEST INFO</span>
    </div>
    <div class="feature">
      <div class="feature-icon"><svg width="30" height="30" viewBox="0 0 30 30"><circle cx="15" cy="15" r="12" fill="none" stroke="#2a8cd8" stroke-width="3" stroke-dasharray="30 8"/><path d="M15 8l-7 6h2v7h10v-7h2z" fill="#2a8cd8"/></svg></div>
      <h3>Looking for a better mortgage?</h3>
      <p>Lorem ipsum dolor sit amet, consectetur adipiscing elit. Vestibulum et dignissim turpis. Maecenas</p>
      <span class="more">Read more</span><span class="btn-pill">REQUEST INFO</span>
    </div>
    <div class="feature">
      <div class="feature-icon"><svg width="34" height="22" viewBox="0 0 34 22"><path d="M1 6l8-4 8 5 8-5 8 4v6l-8 8-4-2-4 2-8-6z" fill="#2a8cd8"/></svg></div>
      <h3>Looking for a better mortgage?</h3>
      <p>Lorem ipsum dolor sit amet, consectetur adipiscing elit. Vestibulum et dignissim turpis. Maecenas</p>
      <span class="more">Read more</span><span class="btn-pill">REQUEST INFO</span>
    </div>
  </div>
</section>

<section class="commercial">
  <div class="wrap">
    <h2 class="section-title">YOUR COMMERCIAL REAL ESTATE SPECIALIST</h2>
    <p class="section-lead">Lorem ipsum dolor sit amet, consectetur adipiscing elit. Vestibulum et dignissim turpis. Maecenas a enim egestas, euismod sem ac, scelerisque magna. Vestibulum blandit consequat purus sed volutpat.</p>
    <div class="property-grid">
      <div class="property-card"><div class="photo" role="img" aria-label="Multi-family brick apartment building" style="background:linear-gradient(180deg,#6d8fb8,#8a4a3a 55%,#5a6a3c)"></div><div class="label">Multi-family residential<b>+</b></div></div>
      <div class="property-card"><div class="photo" role="img" aria-label="Retail storefront building" style="background:linear-gradient(180deg,#9fb6cc,#a86a4c 45%,#7a5a48)"></div><div class="label">Retail<b>+</b></div></div>
      <div class="property-card"><div class="photo" role="img" aria-label="Glass office tower" style="background:linear-gradient(135deg,#c6dbe9,#4f86ad 60%,#2c5a7c)"></div><div class="label">Office<b>+</b></div></div>
      <div class="property-card"><div class="photo" role="img" aria-label="Industrial steel structure" style="background:linear-gradient(180deg,#3e7fbf,#1f4f80 60%,#142e4a)"></div><div class="label">Industrial<b>+</b></div></div>
      <div class="property-card"><div class="photo" role="img" aria-label="Mixed-use brick building" style="background:linear-gradient(180deg,#7fa3cf,#8c4a38 55%,#6a5a48)"></div><div class="label">Mixed-use property<b>+</b></div></div>
      <div class="property-card"><div class="photo" role="img" aria-label="Seniors housing residence" style="background:linear-gradient(180deg,#c9d3da,#8e8a86 55%,#4e6a3a)"></div><div class="label">Seniors housing<b>+</b></div></div>
      <div class="property-card"><div class="photo" role="img" aria-label="Open green land with trees" style="background:linear-gradient(180deg,#2e5a2a,#4f8a36 55%,#7dbb4a)"></div><div class="label">Land<b>+</b></div></div>
      <div class="property-card"><div class="photo" role="img" aria-label="Low-rise building with palm trees" style="background:linear-gradient(180deg,#8fb3d6,#c9b89a 55%,#5a6a4a)"></div><div class="label">Other properties<b>+</b></div></div>
    </div>
  </div>
</section>

<section class="welcome">
  <div class="wrap">
    <div class="welcome-text">
      <h2>Welcome to Maplecrest Mortage group</h2>
      <p>Lorem ipsum dolor sit amet, consectetur adipiscing elit. Vestibulum et dignissim turpis. Maecenas a enim egestas, euismod sem ac, scelerisque magna. Vestibulum blandit consequat purus sed volutpat. Pellentesque malesuada tincidunt eros at rhoncus.</p>
      <h3>Residential Mortgages</h3>
      <p>Lorem ipsum dolor sit amet, consectetur adipiscing elit. Vestibulum et dignissim turpis. Maecenas a enim egestas, euismod sem ac, scelerisque magna.Lorem ipsum dolo</p>
      <p>sit amet, consectetur adipiscing elit. Vestibulum et dignissim turpis. Maecenas a enim egestas, euismod sem ac, scelerisque magnaLorem ipsum dolor sit amet, consectetur adipiscing elit. Vestibulum</p>
      <span class="btn-square">Read more</span>
    </div>
    <div class="link-grid">
      <div class="link-tile"><div class="photo" role="img" aria-label="Hands holding a small model house" style="background:linear-gradient(135deg,#2a2a2a,#c98a5a 55%,#e8d5c0)"></div><span>My Mortgage</span></div>
      <div class="link-tile"><div class="photo" role="img" aria-label="Clock beside stacks of coins" style="background:linear-gradient(135deg,#f1ede4,#d8c27a 60%,#b8902a)"></div><span>Pay down your mortgagefaster</span></div>
      <div class="link-tile"><div class="photo" role="img" aria-label="Model house on a calculator" style="background:linear-gradient(135deg,#d8d8d8,#b04a3a 50%,#6a6a6a)"></div><span>Mortgage calculators</span></div>
      <div class="link-tile"><div class="photo" role="img" aria-label="Broker meeting with a client" style="background:linear-gradient(135deg,#e6e0da,#9a7a66 55%,#4a4a4a)"></div><span>Working with a Mortgage Broker</span></div>
    </div>
  </div>
</section>

<section class="news">
  <div class="wrap">
    <h2 class="section-title">Our Latest News</h2>
    <p class="section-lead">Lorem ipsum dolor sit amet, consectetur adipiscing elit. Vestibulum et dignissim turpis. Maecenas a enim egestas.</p>
    <div class="news-grid">
      <article class="news-card"><div class="photo" role="img" aria-label="Businessman holding a model house" style="background:linear-gradient(135deg,#1e1e1e,#4a3a30 55%,#c2a07a)"></div><h3>Morbi malesuada semper ex quis tristique</h3><p>Integer dictum dolor lacus, vitae lacinia ex egestas ac. Curabitur cursus vel enim id iaculis. Quisque convallis massa a mauris auctor auctor.arcu.</p><span class="more">Read more</span></article>
      <article class="news-card"><div class="photo" role="img" aria-label="Hand holding house keys" style="background:linear-gradient(135deg,#e88a3a,#e8dcc8 50%,#b9c96a)"></div><h3>Morbi malesuada semper ex quis tristique</h3><p>Integer dictum dolor lacus, vitae lacinia ex egestas ac. Curabitur cursus vel enim id iaculis. Quisque convallis massa a mauris auctor auctor.arcu.</p><span class="more">Read more</span></article>
      <article class="news-card"><div class="photo" role="img" aria-label="Business handshake" style="background:linear-gradient(135deg,#111,#3a3a3a 50%,#e8e8e8)"></div><h3>Morbi malesuada semper ex quis tristique</h3><p>Integer dictum dolor lacus, vitae lacinia ex egestas ac. Curabitur cursus vel enim id iaculis. Quisque convallis massa a mauris auctor auctor.arcu.</p><span class="more">Read more</span></article>
    </div>
  </div>
</section>

<section class="testimonials" role="img" aria-label="Blue band over a faint apartment building backdrop">
  <h2>Testimonials</h2>
  <blockquote>I am so happy, my dear friend, so absorbed in the exquisite sense of mere tranquil existence, that I neglect my talents. I should be incapable of drawing a single stroke at the present moment than now.</blockquote>
  <div class="avatar" role="img" aria-label="Client portrait"></div>
  <div class="name">Sam Porter</div>
  <div class="role">Master of Darkness</div>
  <div class="dots"><span class="off"></span><span></span><span></span></div>
</section>

<footer class="site-footer">
  <div class="wrap">
    <div class="footer-about">
      <div class="brand"><div class="brand-square"></div>MAPLECREST</div>
      <p>Duis facilisis lacus sem sed tempor. Etiam blandit maximus ex, ut efficitur ante porttitor ac. Duis sit amet nunc nec dolor ullamcorper fringilla id vel ut ante. Ut facilisis, diam sit amet rhoncus pellentesque, est purus rhoncus dolor, eu tincidunt justo magna id nisl.</p>
      <span class="more">Read more</span>
    </div>
    <div class="footer-col">
      <h4>USEFUL LINKS</h4>
      <ul class="footer-links"><li>About US</li><li>All Listings</li><li>Agents</li><li>Gallery</li><li>Services</li><li>Blog</li><li>Contact US</li></ul>
    </div>
    <div class="footer-col">
      <h4>TWITTER FEED</h4>
      <div class="tweet"><div class="tweet-thumb"></div><p><a>Home Finance Daily</a> @homefin_daily 5 steps to a faster approval this spring. Read the guide: <a>t.co/a1b2c3</a></p></div>
      <div class="tweet"><div class="tweet-thumb"></div><p><a>Lena Brooks</a> @lenabrooks Rates update for first-time buyers, with new figures: <a>t.co/d4e5f6</a> 1 day ago</p></div>
    </div>
    <div class="footer-col">
      <h4>CONTACT INFO</h4>
      <ul class="contact-list">
        <li><svg width="10" height="14" viewBox="0 0 10 14"><path d="M5 0a5 5 0 0 1 5 5c0 4-5 9-5 9S0 9 0 5a5 5 0 0 1 5-5z" fill="#ccc"/><circle cx="5" cy="5" r="2" fill="#3a3c40"/></svg><span>218 Harbour Lane, Lakeview, ON L6K 2A1</span></li>
        <li><svg width="12" height="12" viewBox="0 0 24 24"><path fill="#ccc" d="M6.6 10.8a15 15 0 0 0 6.6 6.6l2.2-2.2c.3-.3.7-.4 1-.2 1.1.4 2.3.6 3.6.6.6 0 1 .4 1 1V20c0 .6-.4 1-1 1C10.6 21 3 13.4 3 4c0-.6.4-1 1-1h3.5c.6 0 1 .4 1 1 0 1.3.2 2.5.6 3.6.1.3 0 .7-.2 1z"/></svg><span>(905)-555-0187</span></li>
        <li><svg width="13" height="10" viewBox="0 0 26 20"><rect x="1" y="1" width="24" height="18" fill="none" stroke="#ccc" stroke-width="2"/><path d="M1 1l12 10 12-10" fill="none" stroke="#ccc" stroke-width="2"/></svg><span style="color:var(--blue)">contact@maplecrest.example</span></li>
      </ul>
      <div class="footer-social"><span></span><span></span><span></span><span></span><span></span></div>
    </div>
  </div>
  <div class="copyright">© Copyright 2016 Maplecrest Mortgage group</div>
</footer>

</body>
</html>
```